Business Card Design Project

I need a business card for an environmentally friendly interior design company called Maplecrest Decor.
I was thinking it might be nice to print the business cards on brown recycled paper with green ink.
In addition to interior design, I will also be able to consult with homeowners regarding their indoor environments and how they might be affecting their health after May 2013 which is when I will complete my certification program. This can be added to the business card at that time: "Certified Dwelling Vitality Environmental Consultant".

```html
<!DOCTYPE html>
<html lang="en">
<head>
<meta charset="utf-8">
<title>Maplecrest Decor — Business Card</title>
<link rel="stylesheet" href="https://fonts.googleapis.com/css2?family=Questrial&family=Arimo:wght@400&display=swap">
<style>
  :root {
    --paper: #e4dfd8;
    --ink-green: #00553d;
    --pale-ink: #ddd8cf;
    --backdrop: #efece7;
  }
  * { margin: 0; padding: 0; box-sizing: border-box; }
  html, body { width: 1200px; height: 900px; overflow: hidden; }
  body {
    background: var(--backdrop);
    position: relative;
    font-family: "Arimo", Arial, sans-serif;
  }
  .card {
    position: absolute;
    left: 250px;
    width: 700px;
    height: 400px;
    overflow: hidden;
    box-shadow: 0 4px 14px rgba(0,0,0,0.18);
  }
  .card--front { top: 35px; background: var(--paper); color: var(--ink-green); }
  .card--back { top: 465px; background: var(--ink-green); color: var(--pale-ink); }

  .divider {
    position: absolute;
    top: 0;
    bottom: 0;
    width: 2px;
  }
  .card--front .divider { left: 250px; background: var(--ink-green); }
  .card--back .divider { left: 225px; background: var(--pale-ink); }

  .base-band {
    position: absolute;
    left: 0; right: 0; bottom: 0;
    height: 24px;
    background: var(--ink-green);
  }

  .wordmark {
    position: absolute;
    font-family: "Questrial", "Century Gothic", sans-serif;
    font-weight: 400;
    letter-spacing: 0.5px;
    white-space: nowrap;
  }
  .card--front .wordmark { left: 282px; top: 100px; font-size: 44px; }
  .card--back .wordmark { left: 262px; top: 112px; font-size: 46px; }

  .contact {
    position: absolute;
    left: 40px;
    top: 262px;
    font-size: 18px;
    line-height: 26px;
  }
  .contact__phone { display: flex; align-items: center; gap: 8px; }
  .contact__phone svg { width: 14px; height: 14px; }

  .services {
    position: absolute;
    left: 272px;
    top: 272px;
    font-size: 14px;
    line-height: 20px;
    list-style: none;
    white-space: nowrap;
  }
</style>
</head>
<body>
  <section class="card card--front" aria-label="Business card front">
    <div class="divider"></div>
    <div class="wordmark">Maplecrest Decor</div>
    <div class="contact">
      <p class="contact__name">Nora Ellis Pratt</p>
      <p class="contact__phone">
        <svg viewBox="0 0 14 14" aria-hidden="true">
          <rect x="2" y="1" width="10" height="12" rx="1.5" fill="none" stroke="currentColor" stroke-width="1.5"/>
          <line x1="4.5" y1="4" x2="9.5" y2="4" stroke="currentColor" stroke-width="1.2"/>
          <line x1="4.5" y1="7" x2="9.5" y2="7" stroke="currentColor" stroke-width="1.2"/>
          <line x1="4.5" y1="10" x2="9.5" y2="10" stroke="currentColor" stroke-width="1.2"/>
        </svg>
        (555) 318-4072
      </p>
    </div>
    <ul class="services">
      <li>Maplecrest Decor</li>
      <li>Environmentally friendly design</li>
      <li>Certified Dwelling Vitality Environmental Consultant</li>
    </ul>
    <div class="base-band"></div>
  </section>

  <section class="card card--back" aria-label="Business card back">
    <div class="divider"></div>
    <div class="wordmark">Maplecrest Decor</div>
  </section>
</body>
</html>
```